BRVL web site redesign

Coastal Linkwork Systems service (BRVL) is a diverse technology company specialising in design and installation of fibre optics, network convergence and building services, for commercial clients in Australia, we required a new design of our website to attract new clients, generate sales leads, and provide information about our services to the market. The site and should have a new technology look and feel and be designed in word press. our branding colour is blue.

Target Market(s)

New developments, Construction organisations, Commercial end users, IT managers, Consultants.

Industry/Entity Type

It Company

Number of Pages Required

5+ page

Font styles to use
Sans Serif

Colors
0292cd
3176b5

Requirements
Must have
• key pages.
• Home page with some sizzle, automated pictures running through, I like the look of this competitor website http://www.tarelmesh.com.au/ good clean menus and easy to navigate.
• Services page our key services are Fibre optics, Security, Building services,Electrical. I would like the same page layout (Design) for all our services, with a find out more link on each page, manly picture driven with text around our key messaging.
• About us page with space for company profile and directors pictures, bio and contact information.
• Certifications / Accreditations page with have over 20 certifications on different products from suppliers, and a number of licences from governing bodies.
• Current and past projects page with case studies and customer outcomes
• Contact us page with options around what services they require more information on, please keep in mind the site is around generating sales Leeds and being seen as an industry expert.
Nice to have
• RSS feeds, Linked in link, to be placed within the design, Consistent BRVL branding,Same colour blue as our logo Document library for education information, white papers, presentations etc,
• a new technology look and feel, mobile friendly.
Should not have
• boring layout, move away from our cuurent website http://www.brvlgroup.com.au/
• no e eCommerce store required.

```html
<!DOCTYPE html>
<html lang="en">
<head>
<meta charset="utf-8">
<title>BRVL – Coastal Linkwork Systems service</title>
<link href="https://fonts.googleapis.com/css2?family=Arimo:wght@400;700&display=swap" rel="stylesheet">
<style>
:root{
  --bar-dark:#4b4b4b;
  --rule-black:#111;
  --paper:#ececec;
  --brand-blue:#0a9fd8;
  --brand-deep:#3176b5;
  --text-grey:#8a8a8a;
  --ring-grey:#b9b9b9;
  --white:#fff;
}
*{margin:0;padding:0;box-sizing:border-box}
html,body{width:1200px;height:999px;overflow:hidden}
body{position:relative;background:var(--paper);font-family:"Arimo",Arial,sans-serif;color:var(--text-grey)}
.top-bar{position:absolute;left:0;top:0;width:1200px;height:40px;background:var(--bar-dark);border-bottom:4px solid var(--rule-black);height:44px}
.utility-links{position:absolute;left:129px;top:13px;display:flex;gap:27px;font-size:14px;color:var(--white)}
.call-us{position:absolute;left:712px;top:13px;font-size:14px;color:var(--white)}
.call-us b{font-weight:700}
.social-dots{position:absolute;left:907px;top:6px;display:flex;gap:4px}
.social-dots span{width:30px;height:30px;border-radius:50%;display:block}
.header{position:absolute;left:0;top:44px;width:1200px;height:103px}
.brand{position:absolute;left:125px;top:7px;display:flex;align-items:center;gap:12px}
.brand-square{width:34px;height:34px;background:var(--brand-blue)}
.brand-name{font-size:50px;font-weight:700;color:var(--brand-blue);letter-spacing:1px;line-height:1}
.brand-tag{position:absolute;left:125px;top:80px;font-size:9px;color:var(--brand-deep);text-transform:uppercase;letter-spacing:.2px}
.main-nav{position:absolute;left:586px;top:28px;width:485px;height:48px;background:var(--brand-blue);display:flex;align-items:center;font-size:14px;color:var(--white)}
.main-nav a{color:inherit;text-decoration:none;position:absolute;top:16px}
.hero{position:absolute;left:0;top:147px;width:1200px;height:436px;border-top:5px solid var(--rule-black);border-bottom:5px solid var(--rule-black);background:linear-gradient(100deg,#3d4a3a 0%,#5a7a3c 14%,#6b5a48 28%,#2c2e31 45%,#3a3c40 65%,#2a3a55 78%,#4f6f9a 90%,#6f5a4a 100%)}
.hero-arrow{position:absolute;top:200px;width:28px;height:28px}
.welcome{position:absolute;left:112px;top:608px;width:968px;text-align:center;font-size:35px;letter-spacing:1.2px;color:#8a8a8a;border-bottom:1px solid #d8d8d8;padding-bottom:2px;line-height:41px}
.welcome span{color:var(--brand-deep)}
.service{position:absolute;top:685px;width:240px;text-align:center}
.service svg{display:block;margin:0 auto}
.service h2{margin-top:20px;font-size:18px;font-weight:400;color:var(--brand-deep);letter-spacing:.5px;border-bottom:1px solid #d8d8d8;padding-bottom:4px;margin-left:14px;margin-right:14px}
.service p{font-size:14px;line-height:15.2px;margin:4px auto 0;width:200px}
.service p a{color:var(--brand-blue);text-decoration:none}
.section-title{position:absolute;top:982px;font-size:22px;color:var(--brand-deep);font-weight:400}
</style>
</head>
<body>
<div class="top-bar">
  <nav class="utility-links"><span>My Account</span><span>Blog</span><span>Sitemap</span></nav>
  <div class="call-us"><b>Call Us:</b> 1300 555 214</div>
  <div class="social-dots" aria-label="Social links">
    <span style="background:#2d5f96"></span><span style="background:#17a9dd"></span><span style="background:#1c86c4"></span><span style="background:#c1351d"></span><span style="background:#ef6a1b"></span>
  </div>
</div>

<header class="header">
  <div class="brand"><div class="brand-square"></div><div class="brand-name">BRVL</div></div>
  <div class="brand-tag">Coastal Linkwork Systems service</div>
  <nav class="main-nav">
    <a style="left:39px">Home</a><a style="left:117px">About Us</a><a style="left:213px">Products</a><a style="left:302px">Services</a><a style="left:394px">Contact</a>
  </nav>
</header>

<section class="hero" role="img" aria-label="Slideshow photo of a fibre optic fusion splicer beside bundled green fibre cables">
  <svg class="hero-arrow" style="left:128px" viewBox="0 0 28 28"><circle cx="14" cy="14" r="12.5" fill="none" stroke="#fff" stroke-width="2"/><path d="M17 7 L9 14 L17 21 Z" fill="#fff"/></svg>
  <svg class="hero-arrow" style="left:1044px" viewBox="0 0 28 28"><circle cx="14" cy="14" r="12.5" fill="none" stroke="#fff" stroke-width="2"/><path d="M11 7 L19 14 L11 21 Z" fill="#fff"/></svg>
</section>

<h1 class="welcome" style="font-weight:400">Welcome to our Website <span>www.brvlgroup.com.au</span></h1>

<div class="service" style="left:121px">
  <svg width="120" height="120" viewBox="0 0 120 120"><circle cx="60" cy="60" r="59" fill="var(--ring-grey)"/><circle cx="60" cy="60" r="49" fill="var(--brand-blue)"/>
    <g fill="none" stroke="#fff" stroke-width="2"><circle cx="60" cy="60" r="17"/><line x1="34" y1="60" x2="86" y2="60"/><line x1="60" y1="34" x2="60" y2="86"/></g><circle cx="60" cy="60" r="6" fill="#fff"/></svg>
  <h2>Commercial Security</h2>
  <p>Lorem ipsum dolor sit amet, consectetuer adipiscing elit. Aenean commodo ligula eget dolor. Aenean massa. Cum sociis natoque penatibus et magnis dis parturient <a>more...</a></p>
</div>

<div class="service" style="left:370px">
  <svg width="120" height="120" viewBox="0 0 120 120"><circle cx="60" cy="60" r="59" fill="var(--ring-grey)"/><circle cx="60" cy="60" r="49" fill="var(--brand-blue)"/>
    <g fill="none" stroke="#fff" stroke-width="2" stroke-linejoin="round"><path d="M52 40 L60 36 L68 48 M62 46 L68 48 L70 42"/><path d="M82 62 L86 70 L78 78 L68 78 M72 74 L68 78 L72 82"/><path d="M48 78 L36 78 L34 70 L42 58 M36 60 L42 58 L44 64"/></g></svg>
  <h2>Data &amp; Fibre</h2>
  <p>Lorem ipsum dolor sit amet, consectetuer adipiscing elit. Aenean commodo ligula eget dolor. Aenean massa. Cum sociis natoque penatibus et magnis dis parturient <a>more...</a></p>
</div>

<div class="service" style="left:602px">
  <svg width="120" height="120" viewBox="0 0 120 120"><circle cx="60" cy="60" r="59" fill="var(--ring-grey)"/><circle cx="60" cy="60" r="49" fill="var(--brand-blue)"/>
    <g fill="none" stroke="#fff" stroke-width="2.5"><circle cx="60" cy="60" r="25"/><ellipse cx="60" cy="60" rx="11" ry="25"/><line x1="35" y1="60" x2="85" y2="60"/><line x1="60" y1="35" x2="60" y2="85"/><path d="M39 47 H81 M39 73 H81"/></g></svg>
  <h2>ICT</h2>
  <p>Lorem ipsum dolor sit amet, consectetuer adipiscing elit. Aenean commodo ligula eget dolor. Aenean massa. Cum sociis natoque penatibus et magnis dis parturient <a>more...</a></p>
</div>

<div class="service" style="left:838px">
  <svg width="120" height="120" viewBox="0 0 120 120"><circle cx="60" cy="60" r="59" fill="var(--ring-grey)"/><circle cx="60" cy="60" r="49" fill="var(--brand-blue)"/>
    <g fill="none" stroke="#fff" stroke-width="1.6"><ellipse cx="60" cy="60" rx="28" ry="10"/><ellipse cx="60" cy="60" rx="28" ry="10" transform="rotate(60 60 60)"/><ellipse cx="60" cy="60" rx="28" ry="10" transform="rotate(-60 60 60)"/></g><circle cx="60" cy="60" r="4" fill="#fff"/></svg>
  <h2>Electrical</h2>
  <p>Lorem ipsum dolor sit amet, consectetuer adipiscing elit. Aenean commodo ligula eget dolor. Aenean massa. Cum sociis natoque penatibus et magnis dis parturient <a>more...</a></p>
</div>

<h2 class="section-title" style="left:128px">Who are We?</h2>
<h2 class="section-title" style="left:626px">Our Projects</h2>
</body>
</html>
```